Private lender of mortgages and rent to own housing

need a website that reflects real estate especially mortgage lending and rent to own houses..
Sections as follows
Home About Types of mortgages Rent to own Contact us
Target Market(s)
consumers who require non traditonal mortgages
Industry/Entity Type
Mortgage
Coding
Coded - Design and coding required
Number of Pages Required
4 page
Font styles to use
Sans Serif
Colors
Designer to choose colors to be used in the design.
Requirements
Must have
- background pictures on pages. with nice picture on homepage of houses or a community
Nice to have
- contact us form i supplied a ink to

```html
<!DOCTYPE html>
<html lang="en">
<head>
<meta charset="utf-8">
<title>Harbourline Lending Group</title>
<link rel="stylesheet" href="https://fonts.googleapis.com/css2?family=Lato:wght@400;700;900&family=Open+Sans:wght@400;600;700&display=swap">
<style>
:root{
  --navy:#2b2870;
  --navy-deep:#221f5e;
  --band:#332f7a;
  --ink:#222222;
  --text:#666666;
  --muted:#888888;
  --line:#d8d8d8;
  --footer:#232323;
  --white:#ffffff;
}
*{box-sizing:border-box;margin:0;padding:0}
html,body{width:1200px;height:2995px;overflow:hidden}
body{position:relative;background:var(--white);font-family:"Open Sans",Arial,sans-serif;color:var(--text)}
.abs{position:absolute}

/* header */
.top-rule{left:0;top:0;width:1200px;height:4px;background:var(--navy)}
.brand{left:96px;top:50px;font-family:"Lato",Arial,sans-serif;font-weight:900;font-size:19px;color:var(--navy);letter-spacing:.3px;display:flex;align-items:center;gap:10px}
.brand .dot{width:16px;height:16px;background:var(--navy);border-radius:50%}
.contact-strip{right:96px;top:22px;font-size:13px;color:#444;display:flex;gap:14px;align-items:center}
.contact-strip svg{width:12px;height:12px;fill:var(--navy);vertical-align:-1px;margin-right:5px}
.contact-strip .sep{color:#aaa}
.main-nav{right:96px;top:62px;display:flex;gap:40px;font-family:"Lato",Arial,sans-serif;font-weight:700;font-size:14.5px;color:var(--ink);letter-spacing:.4px}
.main-nav a{color:inherit;text-decoration:none;position:relative;padding-top:2px}
.main-nav a.active{color:var(--navy)}
.main-nav a.active::before{content:"";position:absolute;left:50%;top:-14px;width:42px;height:12px;margin-left:-21px;background:var(--navy);clip-path:polygon(50% 0,100% 100%,82% 100%,50% 30%,18% 100%,0 100%)}

/* hero */
.hero{left:0;top:104px;width:1200px;height:630px;overflow:hidden}
.hero-photo{position:absolute;inset:0;background:linear-gradient(180deg,#8fb2d8 0%,#b7cfe6 30%,#8c9a8a 52%,#6f9a4a 72%,#5f8f3a 100%)}
.hero-wave{position:absolute;left:0;bottom:0;width:1200px;height:90px}
.hero-title{position:absolute;left:0;width:1200px;top:268px;text-align:center;font-family:"Lato",Arial,sans-serif;font-weight:700;color:var(--white);font-size:44px;line-height:1.25;letter-spacing:.5px;text-shadow:0 2px 6px rgba(0,0,0,.25)}
.hero-arrow{position:absolute;top:262px;width:40px;height:40px;border-radius:50%;background:rgba(40,40,60,.55)}
.hero-arrow svg{width:40px;height:40px;stroke:#fff;stroke-width:2.5;fill:none}

/* section titles */
.section-title{left:0;width:1200px;text-align:center;font-family:"Lato",Arial,sans-serif;font-weight:700;font-size:30px;color:var(--ink);letter-spacing:.5px}
.swoosh{left:494px;width:212px;height:18px}

/* rent to own */
.rent-sub{left:0;top:906px;width:1200px;text-align:center;font-family:"Lato",Arial,sans-serif;font-size:21px;color:#333}
.rent-intro{left:240px;top:958px;width:720px;text-align:center;font-size:12.5px;line-height:26px;color:var(--muted)}
.feature{top:1076px;width:240px;text-align:center}
.feature-icon{width:130px;height:110px;margin:0 auto}
.feature h3{margin-top:24px;font-family:"Lato",Arial,sans-serif;font-weight:400;font-size:15.5px;color:var(--ink);letter-spacing:.3px}
.feature p{margin-top:10px;font-size:12.5px;line-height:25px;color:var(--muted)}

/* welcome band */
.welcome{left:0;top:1388px;width:1200px;height:468px;background:linear-gradient(90deg,var(--band) 0%,#3b3786 60%,#343080 100%)}
.video{left:100px;top:1470px;width:462px;height:304px;border:3px solid var(--white);background:linear-gradient(160deg,#c9d6e2 0%,#9fb2bf 35%,#7a9560 70%,#5d7f3c 100%)}
.play{left:302px;top:1594px;width:58px;height:58px}
.welcome-title{left:614px;top:1466px;color:var(--white);font-family:"Lato",Arial,sans-serif;font-weight:700}
.welcome-title .l1{display:flex;align-items:center;gap:12px;font-size:29px;letter-spacing:.5px}
.welcome-title .l1 span.dot{width:16px;height:16px;border-radius:50%;background:var(--white)}
.welcome-title .l2{font-size:22px;margin-top:6px;letter-spacing:.3px}
.welcome-copy{left:614px;top:1556px;width:496px;color:var(--white);font-size:12.5px;line-height:23px}
.welcome-copy p+p{margin-top:21px}
.btn-ghost{display:inline-block;border:1.5px solid var(--white);color:var(--white);border-radius:20px;font-family:"Lato",Arial,sans-serif;font-weight:700;font-size:12px;letter-spacing:.5px;padding:9px 16px}
.welcome-btn{left:614px;top:1740px}

/* news */
.news-card{top:2036px;width:314px}
.news-img{width:314px;height:220px}
.news-card h4{margin-top:26px;font-family:"Lato",Arial,sans-serif;font-weight:700;font-size:19px;color:var(--ink)}
.meta{margin-top:12px;font-size:12.5px;color:#777;display:flex;align-items:center;gap:8px}
.meta svg{width:11px;height:11px;fill:var(--navy)}
.meta .bar{color:#aaa}
.news-card p{margin-top:14px;font-size:12.5px;line-height:21px;color:#777}
.btn-outline{display:inline-block;margin-top:20px;border:1.5px solid #bbb;color:var(--ink);border-radius:20px;font-family:"Lato",Arial,sans-serif;font-weight:700;font-size:12px;letter-spacing:.5px;padding:9px 17px}

/* footer */
.footer-wave{left:0;top:2552px;width:1200px;height:80px}
.footer{left:0;top:2620px;width:1200px;height:375px;background:var(--footer)}
.foot-brand{left:96px;top:2746px;width:254px;text-align:center;font-family:"Lato",Arial,sans-serif;font-weight:900;font-size:19px;color:var(--white);letter-spacing:.3px}
.socials{left:120px;top:2796px;display:flex;gap:12px}
.socials span{width:28px;height:28px;border:1.5px solid var(--white);border-radius:50%}
.foot-col h5{font-family:"Lato",Arial,sans-serif;font-weight:700;font-size:16px;color:var(--white);letter-spacing:.3px;margin-bottom:18px}
.links{left:402px;top:2690px}
.links li{list-style:none;font-size:12.5px;color:#ddd;line-height:25px}
.newsletter{left:582px;top:2690px;width:270px}
.newsletter p{font-size:12.5px;color:#ddd;line-height:21px}
.newsletter .field{margin-top:12px;width:256px;height:36px;border:1px solid #bbb;color:#eee;font-size:12px;padding:9px 12px}
.newsletter .subscribe{display:inline-block;margin-top:18px;background:var(--navy);color:#fff;border-radius:18px;font-size:11.5px;font-weight:600;padding:9px 16px}
.contact{left:894px;top:2690px;width:230px}
.contact .row{display:flex;gap:14px;font-size:12.5px;color:#ddd;line-height:21px;margin-bottom:18px}
.contact svg{width:13px;height:13px;fill:#fff;flex:none;margin-top:4px}
.foot-rule{left:100px;top:2906px;width:1000px;height:1px;background:#555}
.copyright{left:0;top:2946px;width:1200px;text-align:center;font-size:12px;color:#ddd}
</style>
</head>
<body>

<!-- header -->
<div class="abs top-rule"></div>
<div class="abs brand"><span class="dot"></span>HARBOURLINE LENDING GROUP</div>
<div class="abs contact-strip">
  <span><svg viewBox="0 0 24 24"><path d="M6.6 10.8a15 15 0 0 0 6.6 6.6l2.2-2.2c.3-.3.7-.4 1-.2 1.1.4 2.3.6 3.6.6.6 0 1 .4 1 1V20c0 .6-.4 1-1 1A17 17 0 0 1 3 4c0-.6.4-1 1-1h3.5c.6 0 1 .4 1 1 0 1.3.2 2.5.6 3.6.1.3 0 .7-.2 1z"/></svg>(+1) 555 010 0199</span>
  <span class="sep">|</span>
  <span><svg viewBox="0 0 24 24"><path d="M2 5h20v14H2z M2 5l10 8 10-8" /></svg>info@harbourlinelending.ca</span>
</div>
<nav class="abs main-nav">
  <a class="active">HOME</a><a>ABOUT US</a><a>TYPES OF MORTGAGES</a><a>RENT TO OWN</a><a>CONTACT</a>
</nav>

<!-- hero -->
<section class="abs hero">
  <div class="hero-photo" role="img" aria-label="Photo of a two-storey suburban house with green lawn and curved path under a blue sky"></div>
  <div class="hero-title">HARBOURLINE LENDING<br>GROUP</div>
  <div class="hero-arrow" style="left:16px"><svg viewBox="0 0 40 40"><path d="M23 13l-7 7 7 7"/></svg></div>
  <div class="hero-arrow" style="right:16px"><svg viewBox="0 0 40 40"><path d="M17 13l7 7-7 7"/></svg></div>
  <svg class="hero-wave" viewBox="0 0 1200 90" preserveAspectRatio="none">
    <path d="M0 50 C300 0 700 90 1200 20 L1200 90 L0 90Z" fill="var(--navy)"/>
    <path d="M0 62 C300 20 700 96 1200 40 L1200 90 L0 90Z" fill="#ffffff"/>
  </svg>
</section>

<!-- rent to own -->
<h2 class="abs section-title" style="top:812px">RENT TO OWN A HOME</h2>
<svg class="abs swoosh" style="top:860px" viewBox="0 0 212 18"><path d="M2 14 C60 2 150 2 210 8 C150 8 70 10 2 14Z" fill="var(--navy)"/></svg>
<p class="abs rent-sub">We Can Put You in Your Own Home Today</p>
<p class="abs rent-intro">We know life sometimes delivers challenges and it can be hard to get back on track once you have dealt with challenges. Maybe you have been through a divorce, bankruptcy, consumer proposal, loss of job, work place injury, new to the country, self-employed or some credit related challenges that have you behind the eight ball?</p>

<div class="abs feature" style="left:76px">
  <svg class="feature-icon" viewBox="0 0 130 110">
    <path d="M0 30 L65 0 L130 30 L112 30 L65 10 L18 30Z" fill="var(--navy)"/>
    <circle cx="65" cy="62" r="22" fill="var(--navy)"/>
    <text x="65" y="71" text-anchor="middle" font-family="Lato,sans-serif" font-weight="700" font-size="24" fill="#fff">$</text>
    <path d="M30 98 C55 90 80 90 100 96" stroke="var(--navy)" stroke-width="3" fill="none"/>
  </svg>
  <h3>DOWN PAYMENT</h3>
  <p>We require a minimum down payment Of $10,000 or 3.5% to 4% of total price of the home.</p>
</div>
<div class="abs feature" style="left:342px">
  <svg class="feature-icon" viewBox="0 0 130 110">
    <path d="M0 30 L65 0 L130 30 L112 30 L65 10 L18 30Z" fill="var(--navy)"/>
    <circle cx="70" cy="52" r="14" fill="var(--navy)"/>
    <text x="70" y="58" text-anchor="middle" font-family="Lato,sans-serif" font-weight="700" font-size="16" fill="#fff">$</text>
    <path d="M36 80 L56 72 L78 72 L96 64 L100 70 L80 84 L44 88Z" fill="var(--navy)"/>
    <path d="M30 98 C55 90 80 90 100 96" stroke="var(--navy)" stroke-width="3" fill="none"/>
  </svg>
  <h3>HOUSEHOLD INCOME</h3>
  <p>A general guideline is minimum of $50,000 annually but this depends on the price of home you wish</p>
</div>
<div class="abs feature" style="left:608px">
  <svg class="feature-icon" viewBox="0 0 130 110">
    <path d="M0 30 L65 0 L130 30 L112 30 L65 10 L18 30Z" fill="var(--navy)"/>
    <rect x="50" y="38" width="30" height="40" fill="var(--navy)"/>
    <rect x="56" y="46" width="18" height="3" fill="#fff"/><rect x="56" y="54" width="18" height="3" fill="#fff"/><rect x="56" y="62" width="12" height="3" fill="#fff"/>
    <circle cx="80" cy="76" r="9" fill="#fff" stroke="var(--navy)" stroke-width="3"/>
    <path d="M76 76l3 3 5-5" stroke="var(--navy)" stroke-width="2.5" fill="none"/>
    <path d="M30 98 C55 90 80 90 100 96" stroke="var(--navy)" stroke-width="3" fill="none"/>
  </svg>
  <h3>CREDIT REPORT</h3>
  <p>Although your credit won't necessarily disqualify you from our rent to own program, it is important</p>
</div>
<div class="abs feature" style="left:874px">
  <svg class="feature-icon" viewBox="0 0 130 110">
    <path d="M0 30 L65 0 L130 30 L112 30 L65 10 L18 30Z" fill="var(--navy)"/>
    <path d="M46 58 L65 42 L84 58 L84 80 L46 80Z" fill="var(--navy)"/>
    <rect x="60" y="66" width="10" height="14" fill="#fff"/>
    <path d="M30 98 C55 90 80 90 100 96" stroke="var(--navy)" stroke-width="3" fill="none"/>
  </svg>
  <h3>SELECTING A HOUSE</h3>
  <p>May not seem like a strong determining factor overall for qualifying for rent to own but it is for us.</p>
</div>

<!-- welcome band -->
<section class="abs welcome" role="img" aria-label="Navy band over a faint photo of homes"></section>
<div class="abs video" role="img" aria-label="Video still of a couple shaking hands with an agent in front of a house"></div>
<svg class="abs play" viewBox="0 0 58 58"><circle cx="29" cy="29" r="28" fill="rgba(40,40,40,.6)"/><path d="M23 18 L40 29 L23 40Z" fill="#fff"/></svg>
<div class="abs welcome-title">
  <div class="l1"><span class="dot"></span>WELCOME TO</div>
  <div class="l2">HARBOURLINE LENDING GROUP</div>
</div>
<div class="abs welcome-copy">
  <p>Harbourline Lending Group is a private lender of 1 st ,2 nd , construction and bridge mortgages in Maple County area. HLG offers a wide array of financing options to provide assistance to those of you that do not meet the bank's criteria.</p>
  <p>The reasons could range from bruised credit to inability to provide the banks with the required documentation to meet income qualification guidelines or simply you need a short term solution and the bank isn't an option.</p>
</div>
<span class="abs btn-ghost welcome-btn">READ MORE</span>

<!-- latest news -->
<h2 class="abs section-title" style="top:1932px">LATEST NEWS</h2>
<svg class="abs swoosh" style="top:1980px" viewBox="0 0 212 18"><path d="M2 14 C60 2 150 2 210 8 C150 8 70 10 2 14Z" fill="var(--navy)"/></svg>

<article class="abs news-card" style="left:98px">
  <div class="news-img" role="img" aria-label="Photo of a stone and timber family house with a front lawn" style="background:linear-gradient(180deg,#7fb0e0 0%,#a9c6e0 35%,#8a7260 60%,#5f8a3a 100%)"></div>
  <h4>Finibus Bonorum Llanditet Ma</h4>
  <div class="meta"><svg viewBox="0 0 12 12"><rect x="1" y="2" width="10" height="9"/></svg>02/08/2017<span class="bar">|</span><svg viewBox="0 0 12 12"><circle cx="6" cy="3.5" r="2.5"/><path d="M1 12c0-3 2-5 5-5s5 2 5 5z"/></svg>John Doe</div>
  <p>Nam libero tempore, cum soluta nobis est eligendi optio cumque nihil impedit quo minus id quod ma ixime placeat facere possimus</p>
  <span class="btn-outline">READ MORE</span>
</article>
<article class="abs news-card" style="left:444px">
  <div class="news-img" role="img" aria-label="Photo of hands passing a stack of banknotes" style="background:linear-gradient(135deg,#eef0f2 0%,#e7c2a4 45%,#c98a63 65%,#eef0f2 100%)"></div>
  <h4>Finibus Bonorum Llanditet Ma</h4>
  <div class="meta"><svg viewBox="0 0 12 12"><rect x="1" y="2" width="10" height="9"/></svg>02/08/2017<span class="bar">|</span><svg viewBox="0 0 12 12"><circle cx="6" cy="3.5" r="2.5"/><path d="M1 12c0-3 2-5 5-5s5 2 5 5z"/></svg>John Doe</div>
  <p>Nam libero tempore, cum soluta nobis est eligendi optio cumque nihil impedit quo minus id quod ma ixime placeat facere possimus</p>
  <span class="btn-outline">READ MORE</span>
</article>
<article class="abs news-card" style="left:788px">
  <div class="news-img" role="img" aria-label="Photo of a modern white two-storey house with palm trees" style="background:linear-gradient(180deg,#dfe6ec 0%,#d9d3c6 50%,#b7b0a2 80%,#7a8a5c 100%)"></div>
  <h4>Finibus Bonorum Llanditet Ma</h4>
  <div class="meta"><svg viewBox="0 0 12 12"><rect x="1" y="2" width="10" height="9"/></svg>02/08/2017<span class="bar">|</span><svg viewBox="0 0 12 12"><circle cx="6" cy="3.5" r="2.5"/><path d="M1 12c0-3 2-5 5-5s5 2 5 5z"/></svg>John Doe</div>
  <p>Nam libero tempore, cum soluta nobis est eligendi optio cumque nihil impedit quo minus id quod ma ixime placeat facere possimus</p>
  <span class="btn-outline">READ MORE</span>
</article>

<!-- footer -->
<div class="abs footer"></div>
<svg class="abs footer-wave" viewBox="0 0 1200 80" preserveAspectRatio="none">
  <path d="M0 80 L0 40 C350 -10 800 80 1200 8 L1200 80Z" fill="var(--navy-deep)"/>
  <path d="M0 80 L0 60 C350 20 800 96 1200 34 L1200 80Z" fill="var(--footer)"/>
</svg>
<div class="abs foot-brand">HARBOURLINE LENDING GROUP</div>
<div class="abs socials"><span></span><span></span><span></span><span></span><span></span></div>

<div class="abs foot-col links">
  <h5>QUICK LINKS</h5>
  <ul><li>Home</li><li>About Us</li><li>Services</li><li>Rent to own</li><li>Types of mortgages</li><li>Contact us</li></ul>
</div>
<div class="abs foot-col newsletter">
  <h5>NEWSLETTER SUBSCRIPTION</h5>
  <p>Register your Email Address to get Information about us</p>
  <div class="field">Email Address</div>
  <span class="subscribe">SUBSCRIBE</span>
</div>
<div class="abs foot-col contact">
  <h5>CONTACT US</h5>
  <div class="row"><svg viewBox="0 0 24 24"><path d="M12 2a7 7 0 0 0-7 7c0 5 7 13 7 13s7-8 7-13a7 7 0 0 0-7-7zm0 9.5A2.5 2.5 0 1 1 12 6.5a2.5 2.5 0 0 1 0 5z"/></svg><span>Old Simple Street, Old City,<br>New State</span></div>
  <div class="row"><svg viewBox="0 0 24 24"><path d="M6.6 10.8a15 15 0 0 0 6.6 6.6l2.2-2.2c.3-.3.7-.4 1-.2 1.1.4 2.3.6 3.6.6.6 0 1 .4 1 1V20c0 .6-.4 1-1 1A17 17 0 0 1 3 4c0-.6.4-1 1-1h3.5c.6 0 1 .4 1 1 0 1.3.2 2.5.6 3.6.1.3 0 .7-.2 1z"/></svg><span>(+1) 555 010 0199</span></div>
  <div class="row"><svg viewBox="0 0 24 24"><path d="M2 5h20v14H2zm2 2v.5l8 6 8-6V7z"/></svg><span>info@harbourlinelending.ca</span></div>
</div>
<div class="abs foot-rule"></div>
<p class="abs copyright">© Copyright 2017 Harbourline Lending Group. All Rights Reserved</p>

</body>
</html>
```